Sleek business card design for digital agency.

Brief document attached for detailed description and inspiration. Looking for a minimalist sleek, cool, modern business card design.

Industry/Entity Type

Digital

```html
<!DOCTYPE html>
<html lang="en">
<head>
<meta charset="utf-8">
<title>Vantage Works – Business Card</title>
<link href="https://fonts.googleapis.com/css2?family=Open+Sans:wght@300;400;600&display=swap" rel="stylesheet">
<style>
  :root {
    --bg: #e6e6e6;
    --ink: #0b0b0b;
    --paper: #f7f7f5;
    --paper-shade: #ececea;
    --on-ink: #ffffff;
    --mute: #3a3a3a;
    --ghost: #262626;
  }
  * { box-sizing: border-box; margin: 0; padding: 0; }
  html, body { width: 1200px; height: 1000px; overflow: hidden; }
  body {
    background: var(--bg);
    font-family: "Open Sans", Arial, sans-serif;
    color: var(--ink);
    position: relative;
  }
  .card {
    position: absolute;
    left: 250px;
    width: 700px;
    height: 420px;
    border-radius: 18px;
    background: var(--ink);
    box-shadow: 0 10px 30px rgba(0,0,0,.18);
  }
  .card--front { top: 60px; padding: 14px; }
  .card--back { top: 520px; overflow: hidden; }

  .front-face {
    position: relative;
    width: 100%;
    height: 100%;
    border-radius: 6px;
    background: linear-gradient(135deg, var(--paper) 0%, var(--paper-shade) 100%);
    overflow: hidden;
  }
  .brand-tab {
    position: absolute;
    left: 30px; top: 0;
    width: 150px; height: 160px;
    background: var(--ink);
    border-radius: 0 0 75px 75px;
    display: flex; align-items: flex-end; justify-content: center;
    padding-bottom: 52px;
  }
  .brand-tab__name {
    color: var(--on-ink);
    font-weight: 400;
    font-size: 16px;
    letter-spacing: .5px;
  }
  .identity { position: absolute; left: 30px; top: 170px; }
  .identity__name {
    font-weight: 300;
    font-size: 40px;
    line-height: 1.05;
    letter-spacing: .5px;
  }
  .identity__tag {
    display: inline-block;
    background: var(--ink);
    color: var(--on-ink);
    margin-top: 4px;
    padding: 3px 8px 4px;
    line-height: 1.3;
    font-weight: 400;
  }
  .identity__tag span { display: block; font-size: 12px; font-weight: 300; }
  .identity__tag .role { letter-spacing: 1px; text-transform: uppercase; font-size: 13px; font-weight: 400; }

  .contact {
    position: absolute;
    left: 30px; bottom: 36px;
    font-style: normal;
    font-size: 12px;
    font-weight: 300;
    line-height: 1.4;
    color: var(--mute);
  }
  .contact .caps { text-transform: uppercase; }
  .zigzag { position: absolute; left: 0; bottom: 0; width: 250px; height: 26px; }

  .social {
    position: absolute;
    right: 26px; bottom: 30px;
    text-align: right;
    font-size: 13px;
    font-weight: 300;
    color: var(--mute);
    line-height: 1.8;
  }
  .social__item { display: flex; align-items: center; justify-content: flex-end; gap: 7px; }
  .social__dot { width: 9px; height: 9px; border-radius: 50%; background: var(--ink); }

  .back-face {
    width: 100%; height: 100%;
    display: flex; align-items: center; justify-content: center;
    background: linear-gradient(160deg, #151515 0%, #050505 60%, #111 100%);
  }
  .back-face__name {
    color: var(--ghost);
    font-weight: 600;
    font-size: 76px;
    letter-spacing: 1px;
  }
</style>
</head>
<body>
  <section class="card card--front" aria-label="Business card front">
    <div class="front-face">
      <div class="brand-tab">
        <span class="brand-tab__name">Vantage Works</span>
      </div>

      <div class="identity">
        <h1 class="identity__name">Daniel Hewitt</h1>
        <p class="identity__tag"><span class="role">Marketing Director</span><span>Drink order: G&amp;T with cucumber</span></p>
      </div>

      <address class="contact">
        0400 512 987<br>
        03 9000 4182<br>
        dhewitt@vantageworks.com<br>
        <span class="caps">Level 2, 18 Carrow St</span><br>
        <span class="caps">East Hallet SA 5010</span>
      </address>

      <svg class="zigzag" viewBox="0 0 250 26" preserveAspectRatio="none" aria-hidden="true">
        <polygon fill="#0b0b0b" points="0,26 0,6 15,20 30,6 45,20 60,6 75,20 90,6 105,20 120,6 135,20 150,6 165,20 180,6 195,20 210,6 225,20 250,6 250,26"/>
      </svg>

      <div class="social">
        <p class="social__item"><span class="social__dot"></span>@dhewitt81</p>
        <p class="social__item"><span class="social__dot"></span>social.com/vantageworks</p>
      </div>
    </div>
  </section>

  <section class="card card--back" aria-label="Business card back">
    <div class="back-face">
      <span class="back-face__name">Vantage Works</span>
    </div>
  </section>
</body>
</html>
```